Lanternfield - Afro Jazz CD Cover design project

CD Cover design for a jazz album. Starting off as a single/ep release; and then full album release a month later. So cover presentation for box set (physical print) and online distribution. Also alternate cover presentation for movement from EP to full album.
Songs on Ep:Red Kites; Lanternfield; Tin Harbor; Kolo Meti

Music is Afro Jazz. Album Title is: Lanternfield
Artist: Tobias
Producer: Tobias R
Releasing label: RV Music

Project Deadline Extended Reason: My apologies for the inconvenience to everyone. Not well enough to review all designs by today's set deadline. I hope to start doing so and providing feedback in the next few days. Thank you for your submissions. Please continue to submit. Added Wednesday, October 7, 2015

Project Deadline Extended Reason: Hi, Forgive my lack of feedback for the most part; unforseen circumstances. I have looked at some of the designs though and commented on a few. I am of the opinion there could be vast improvements and so am going to provide a 5 day extension as well as a $50 increase in the price money to hopefully inspire greater looking designs and concepts. Thank you. Added Friday, October 30, 2015

Hi guys. I am so sorry I have taken so long. I have considered the designs presented and there are some good concepts there. I must say however that I have not found one that stands out and captivates me. I am left with the choice of selecting among the short list or increasing the amount by another $30 or $50 and hoping for that elusive one, that one of you may yet come up with; what do you think.

Target Market(s)

Global; late teens to fifties; cross cultural

Font styles to use
Script

Requirements
Must have
• Cover (online); Box set (physical print)
• Alternate cover (EP and Album release)
Nice to have
• Creativity and originality. Covers that attract attention, a work of art in itself, evoking an emotional response on its own merits. Remember this is Afro Jazz, not just for Afro audience but global.

```html
<!DOCTYPE html>
<html lang="en">
<head>
<meta charset="utf-8">
<title>Lanternfield – Back Cover</title>
<link rel="stylesheet" href="https://fonts.googleapis.com/css2?family=Open+Sans:wght@300;400&family=Oswald:wght@600&display=swap">
<style>
  :root {
    --teal-bright: #0f7a78;
    --teal-mid: #0a4a4a;
    --teal-deep: #04201f;
    --ink-dark: #021414;
    --text-light: #e6eeee;
    --text-soft: #d2dddd;
  }
  * { margin: 0; padding: 0; box-sizing: border-box; }
  html, body {
    width: 1200px; height: 951px; overflow: hidden;
    background: var(--ink-dark);
  }
  .back-cover {
    position: relative; width: 1200px; height: 951px; overflow: hidden;
    font-family: "Open Sans", sans-serif; color: var(--text-light);
  }
  .backdrop { position: absolute; inset: 0; width: 100%; height: 100%; }

  .spine-title {
    position: absolute;
    font-family: "Oswald", sans-serif; font-weight: 600;
    font-size: 24px; letter-spacing: 0.3px; color: #fff;
    white-space: nowrap; line-height: 1;
    text-shadow: 0 0 14px rgba(180, 240, 240, 0.55);
  }
  .spine-title--left {
    left: 50px; top: 475px;
    transform: translate(-50%, -50%) rotate(-90deg);
  }
  .spine-title--right {
    left: 1152px; top: 475px;
    transform: translate(-50%, -50%) rotate(90deg);
  }

  .tracklist {
    position: absolute; left: 510px; top: 276px;
    list-style: none; font-weight: 300; font-size: 19.5px;
    letter-spacing: 0.3px;
  }
  .tracklist li { height: 67.6px; line-height: 28px; white-space: nowrap; }

  .credits {
    position: absolute; top: 621px; font-weight: 300;
    font-size: 19.5px; letter-spacing: 0.3px; white-space: nowrap;
  }
  .credits--producer { left: 372px; }
  .credits--artist { left: 676px; }

  .label-name {
    position: absolute; left: 133px; top: 760px;
    font-weight: 300; font-size: 13.5px; line-height: 18px;
    letter-spacing: 0.4px; color: var(--text-light); white-space: nowrap;
  }

  .legal {
    position: absolute; left: 131px; top: 792px;
    font-weight: 300; font-size: 13.5px; line-height: 16.3px; color: var(--text-soft);
  }
  .legal span { display: block; white-space: nowrap; }
</style>
</head>
<body>
<main class="back-cover">
  <svg class="backdrop" viewBox="0 0 1200 951" preserveAspectRatio="none" role="img" aria-label="Abstract artwork of shattered teal glass shards on a dark background">
    <defs>
      <radialGradient id="shard-glow-left" cx="0.05" cy="0.2" r="0.55">
        <stop offset="0" stop-color="#0f7a78"/>
        <stop offset="0.6" stop-color="#0a4a4a" stop-opacity="0.7"/>
        <stop offset="1" stop-color="#04201f" stop-opacity="0"/>
      </radialGradient>
      <radialGradient id="shard-glow-right" cx="0.95" cy="0.35" r="0.45">
        <stop offset="0" stop-color="#0d5f5e"/>
        <stop offset="1" stop-color="#04201f" stop-opacity="0"/>
      </radialGradient>
      <linearGradient id="shard-base" x1="0" y1="0" x2="0" y2="1">
        <stop offset="0" stop-color="#063332"/>
        <stop offset="0.5" stop-color="#031818"/>
        <stop offset="1" stop-color="#042120"/>
      </linearGradient>
    </defs>
    <rect width="1200" height="951" fill="url(#shard-base)"/>
    <rect width="1200" height="951" fill="url(#shard-glow-left)"/>
    <rect width="1200" height="951" fill="url(#shard-glow-right)"/>
  </svg>

  <div class="spine-title spine-title--left">LANTERNFIELD</div>
  <div class="spine-title spine-title--right">LANTERNFIELD</div>

  <ol class="tracklist">
    <li>1. RED KITES</li>
    <li>2. LANTERNFIELD</li>
    <li>3. TIN HARBOR</li>
    <li>4. KOLO METI</li>
  </ol>

  <p class="credits credits--producer">PRODUCER - TOBIAS R</p>
  <p class="credits credits--artist">ARTIST- TOBIAS</p>

  <div class="label-name">RV MUSIC</div>

  <p class="legal">
    <span>2015 All rights reserved, consectetuer adipiscing elit. Aenean commodo</span>
    <span>ligula eget dolor. Aenean massa. Cum sociis natoque penatibus et magnis</span>
    <span>dis parturient montes, nascetur ridiculus mus. Donec quam felis, ultricies</span>
    <span>nec, pellentesque eu, pretium quis, sem. Nulla consequat massa quis enim.</span>
    <span>Donec pede justo, fringilla vel, aliquet nec, vulputate eget, arcu. In enim</span>
    <span>justo, rhoncus ut, imperdiet a, venenatis vitae, justo. Nullam dictum felis eu</span>
  </p>
</main>
</body>
</html>
```